Weight Loss Challenge Social Media Graphics

Create 6-7 individual social media graphics (square size) to encourage folks to join our weight loss challenge. For the color scheme of the graphics, use the color palette attached

Note: each graphic can contain any of the stock photography attached or just the single picture of me (brown shirt) but a few should be ONLY the text
For some graphics we can say: JOIN US!
For some graphics, use only TEXT based

Target Market(s)

primarily women who want to get healthy

Industry/Entity Type

health and weight loss

Requirements
Must have
• The largest text should be: Ninety Days Bold

```html
<!DOCTYPE html>
<html lang="en">
<head>
<meta charset="utf-8">
<title>45 Strong Challenge – Social Graphics</title>
<link href="https://fonts.googleapis.com/css2?family=Poppins:wght@400;500;600;700;800&family=Oswald:wght@400;500;600&family=Merriweather:wght@700;900&display=swap" rel="stylesheet">
<style>
  :root{
    --canvas:#170709;
    --cream:#f8f1ec;
    --sand:#eed9cc;
    --mauve:#b48e86;
    --mauve-deep:#9e7770;
    --rose-bg:#b99791;
    --rose-light:#c9a9a2;
    --blush:#f9c6d4;
    --blush-soft:#fde4ec;
    --berry:#a34f63;
    --berry-soft:#b5607a;
    --maroon:#5a2320;
    --cocoa:#7a4e33;
    --ink:#111111;
    --white:#ffffff;
    --shell:#f2f0ef;
    --beige:#efdccc;
  }
  *{box-sizing:border-box;margin:0;padding:0}
  html,body{width:1200px;height:1044px;overflow:hidden;background:var(--canvas)}
  body{position:relative;font-family:'Poppins',sans-serif}
  .card{position:absolute;width:298px;height:298px;overflow:hidden}
  .card svg.bg{position:absolute;inset:0;width:298px;height:298px}
  .photo{position:absolute}
  .t{position:absolute;transform:translateY(-50%);white-space:nowrap;line-height:1}
  .center{left:0;right:0;text-align:center}
  .kicker{font-weight:700;font-size:16px;letter-spacing:.1px}
  .headline{font-weight:800;color:var(--ink)}
  .serif{font-family:'Merriweather',serif;font-weight:900}
  .cond{font-family:'Oswald',sans-serif}

  .card-frame{left:115px;top:193px;background:var(--cream)}
  .card-rose{left:446px;top:193px;background:var(--rose-bg)}
  .card-blush{left:776px;top:193px;background:var(--blush)}
  .card-portrait{left:115px;top:519px;background:var(--white)}
  .card-group{left:446px;top:519px;background:var(--white)}
  .card-hex{left:776px;top:519px;background:var(--shell)}
</style>
</head>
<body>

<section class="card card-frame">
  <svg class="bg" viewBox="0 0 298 298">
    <path d="M0 0H108C70 10 40 40 36 85C30 85 10 88 0 92Z" fill="var(--mauve)"/>
    <path d="M108 0H298V60C260 90 230 110 200 170C170 230 90 240 60 298H0V92C10 88 30 85 36 85C40 40 70 10 108 0Z" fill="var(--sand)" opacity=".55"/>
    <path d="M298 170C280 190 270 240 250 270C235 290 215 292 200 298H298Z" fill="var(--mauve)"/>
    <circle cx="32" cy="100" r="24" fill="var(--mauve)"/>
    <rect x="30" y="182" width="237" height="68" fill="none" stroke="var(--mauve-deep)" stroke-width="0.8"/>
    <rect x="104" y="240" width="90" height="20" fill="var(--cream)"/>
  </svg>
  <div class="photo" role="img" aria-label="Group of smiling adults flexing in a gym" style="left:45px;top:94px;width:207px;height:137px;border-radius:12px;background:linear-gradient(180deg,#a9c2d8 0%,#c79a82 45%,#5b4036 80%,#1e1a1c 100%)"></div>
  <div class="t kicker" style="left:76px;top:27px;color:var(--maroon)">45 STRONG CHALLENGE</div>
  <div class="t headline" style="left:41px;top:58px;font-size:25px">NINETY DAYS BOLD</div>
  <div class="t" style="left:45px;width:207px;text-align:center;top:200px;color:var(--white);font-size:14px">LOSE UP TO 20 POUNDS</div>
  <div class="t" style="left:45px;width:207px;text-align:center;top:219px;color:var(--white);font-size:14px">IN 6 WEEKS!</div>
  <div class="t center" style="top:249px;font-size:13px;font-weight:600;color:var(--ink)">Begins <span style="color:var(--maroon)">Monday, Jan 6th</span></div>
  <div style="position:absolute;left:102px;top:265px;width:94px;height:21px;border-radius:11px;background:var(--mauve);color:var(--cream);font-size:15px;font-weight:700;line-height:21px;text-align:center">JOIN US!</div>
</section>

<section class="card card-rose">
  <svg class="bg" viewBox="0 0 298 298">
    <path d="M0 0H60C30 40 20 80 40 120C60 150 120 160 150 150V0Z" fill="var(--rose-light)" opacity=".6"/>
    <circle cx="165" cy="120" r="120" fill="var(--rose-light)" opacity=".45"/>
    <path d="M298 150C270 200 250 240 260 298H298Z" fill="var(--rose-light)" opacity=".5"/>
    <rect x="26" y="164" width="245" height="54" rx="7" fill="#f3e2d6" stroke="#e7cbb9" stroke-width="1.2"/>
    <line x1="37" y1="277" x2="63" y2="277" stroke="var(--white)" stroke-width="0.8"/>
    <line x1="233" y1="277" x2="259" y2="277" stroke="var(--white)" stroke-width="0.8"/>
  </svg>
  <div class="photo" role="img" aria-label="Four smiling women in sports bras posing together" style="left:26px;top:40px;width:236px;height:125px;border-radius:60px 60px 0 0;background:linear-gradient(180deg,#b08a80 0%,#d7b1a3 35%,#c48fa5 65%,#6c5770 100%)"></div>
  <div class="t center kicker" style="top:22px;color:var(--ink)">45 STRONG CHALLENGE</div>
  <div class="t headline" style="left:26px;width:245px;text-align:center;top:192px;font-size:21px;color:var(--maroon)">NINETY DAYS BOLD</div>
  <div class="t center" style="top:235px;color:var(--white);font-size:15px;font-weight:500">LOSE UP TO 20 POUNDS</div>
  <div class="t center" style="top:255px;color:var(--white);font-size:15px;font-weight:500">IN 6 WEEKS!</div>
  <div class="t center" style="top:277px;color:var(--white);font-size:12.5px;font-weight:500">Begins Monday, Jan 6th</div>
</section>

<section class="card card-blush">
  <svg class="bg" viewBox="0 0 298 298">
    <path d="M0 0H190C185 30 205 60 250 70C285 78 298 110 298 140V160H0Z" fill="var(--white)"/>
    <path d="M190 0C185 30 205 60 250 70C285 78 298 110 298 140" fill="none" stroke="var(--blush)" stroke-width="1"/>
    <rect x="-20" y="110" width="268" height="36" rx="18" fill="var(--white)" stroke="#f4b7c8" stroke-width="1"/>
    <path d="M0 150H298V298H0Z" fill="var(--blush-soft)"/>
    <path d="M0 268C80 250 210 250 298 268V298H0Z" fill="var(--blush)"/>
  </svg>
  <div class="photo" role="img" aria-label="Five women in athletic tops hugging and smiling" style="left:4px;top:148px;width:288px;height:110px;border-radius:0 0 50% 50% / 0 0 14px 14px;background:linear-gradient(180deg,#6b4a3c 0%,#c9967d 35%,#e4c2aa 55%,#2a2224 100%)"></div>
  <div class="t kicker" style="left:10px;top:19px;color:var(--berry-soft)">45 STRONG CHALLENGE</div>
  <div class="t headline" style="left:10px;top:52px;font-size:31px">NINETY</div>
  <div class="t headline" style="left:10px;top:88px;font-size:31px">DAYS BOLD</div>
  <div class="t" style="left:200px;width:100px;text-align:center;top:19px;font-size:15px;color:var(--ink)">Begins</div>
  <div class="t" style="left:200px;width:100px;text-align:center;top:37px;font-size:15px;font-weight:700;color:var(--ink)">Monday</div>
  <div class="t" style="left:200px;width:100px;text-align:center;top:55px;font-size:15px;font-weight:700;color:var(--ink)">Jan 6th</div>
  <div class="t" style="left:10px;top:128px;font-size:12px;color:var(--ink)">LOSE UP TO 20 POUNDS IN 6 WEEKS!</div>
  <div class="t center headline" style="top:279px;font-size:20px">JOIN US!</div>
</section>

<section class="card card-portrait">
  <svg class="bg" viewBox="0 0 298 298">
    <path d="M0 0H298V298H0Z" fill="#fdf6f8"/>
    <path d="M0 0H250C270 20 298 25 298 60V0Z" fill="var(--blush-soft)"/>
    <path d="M0 240C40 220 90 240 100 298H0Z" fill="var(--blush-soft)"/>
    <circle cx="199" cy="203" r="95" fill="#f9c8d6"/>
    <circle cx="199" cy="203" r="88" fill="var(--cocoa)"/>
  </svg>
  <div class="photo" role="img" aria-label="Smiling woman in a tan turtleneck and black trousers, hand on hip" style="left:172px;top:37px;width:124px;height:253px;border-radius:62px 62px 10px 10px;background:linear-gradient(180deg,#6a4634 0%,#c49472 25%,#b68866 55%,#1c1a1c 80%)"></div>
  <div class="t kicker" style="left:16px;top:22px;color:var(--berry)">45 STRONG CHALLENGE</div>
  <div class="t headline" style="left:14px;top:55px;font-size:25px">NINETY</div>
  <div class="t headline" style="left:14px;top:93px;font-size:25px">DAYS BOLD</div>
  <div class="t" style="left:10px;top:142px;font-size:14px;color:var(--ink)">LOSE UP TO</div>
  <div class="t" style="left:10px;top:164px;font-size:14px;color:var(--ink)">20 POUNDS</div>
  <div class="t" style="left:10px;top:186px;font-size:14px;color:var(--ink)">IN 6WEEKS!</div>
  <div class="t" style="left:11px;top:250px;font-size:14px;color:var(--berry)">Begins</div>
  <div class="t" style="left:11px;top:266px;font-size:14px;font-weight:700;color:var(--ink)">Monday</div>
  <div class="t" style="left:11px;top:283px;font-size:14px;font-weight:700;color:var(--ink)">Jan 6th</div>
</section>

<section class="card card-group">
  <svg class="bg" viewBox="0 0 298 298">
    <path d="M0 0H60C45 50 45 110 75 150H0Z" fill="#f7b6c9"/>
    <path d="M200 190C240 180 280 185 298 200V298H180Z" fill="#f9c6d4"/>
    <rect x="96" y="84" width="182" height="64" rx="32" fill="#fdeef2" stroke="#f3a9bf" stroke-width="1" stroke-dasharray="2 2"/>
  </svg>
  <div class="photo" role="img" aria-label="Four women in colourful sports bras and leggings standing arm in arm" style="left:0;top:150px;width:196px;height:148px;background:linear-gradient(180deg,#4a3530 0%,#d4a58f 30%,#c889a4 60%,#8f9ab8 100%)"></div>
  <div class="t kicker" style="left:85px;width:180px;text-align:center;top:25px;color:var(--berry-soft)">45 STRONG CHALLENGE</div>
  <div class="t headline" style="left:62px;width:228px;text-align:center;top:53px;font-size:22px">NINETY DAYS BOLD</div>
  <div class="t" style="left:96px;width:182px;text-align:center;top:108px;font-size:12px;color:var(--ink)">LOSE UP TO 20 POUNDS</div>
  <div class="t" style="left:96px;width:182px;text-align:center;top:124px;font-size:12px;color:var(--ink)">IN 6 WEEKS!</div>
  <div class="t" style="left:202px;top:166px;font-size:11px;font-weight:600;color:var(--berry)">Begins Monday,</div>
  <div class="t" style="left:202px;top:178px;font-size:11px;font-weight:600;color:var(--berry)">Jan 6th</div>
  <div class="t serif" style="left:200px;width:84px;text-align:center;top:276px;font-size:14px;color:var(--white)">JOIN US !</div>
</section>

<section class="card card-hex">
  <svg class="bg" viewBox="0 0 298 298">
    <polygon points="117,174 161,76 298,76 298,261 164,261" fill="var(--beige)" stroke="var(--white)" stroke-width="5"/>
    <polygon points="0,151 77,151 129,298 0,298" fill="var(--mauve)"/>
    <circle cx="105" cy="268" r="38" fill="#f2e2d4" stroke="var(--white)" stroke-width="2"/>
  </svg>
  <div class="photo" role="img" aria-label="Smiling woman in a tan turtleneck and black trousers, hand on hip" style="left:180px;top:16px;width:118px;height:245px;border-radius:56px 56px 0 0;background:linear-gradient(180deg,#6a4634 0%,#c49472 25%,#b68866 55%,#1c1a1c 85%)"></div>
  <div class="t cond" style="left:18px;top:27px;font-size:17px;font-weight:600;color:var(--maroon)">45 STRONG CHALLENGE</div>
  <div class="t cond" style="left:16px;top:63px;font-size:33px;font-weight:600;color:var(--ink)">NINETY</div>
  <div class="t cond" style="left:16px;top:103px;font-size:33px;font-weight:600;color:var(--ink)">DAYS BOLD</div>
  <div class="t cond" style="left:9px;top:184px;font-size:18px;color:#f6e6dd">LOSE UP TO</div>
  <div class="t cond" style="left:9px;top:206px;font-size:18px;color:#f6e6dd">20 POUND IN</div>
  <div class="t cond" style="left:9px;top:228px;font-size:18px;color:#f6e6dd">6WEEKS!</div>
  <div class="t" style="left:67px;width:76px;text-align:center;top:253px;font-size:13px;font-weight:600;color:var(--ink)">Begins</div>
  <div class="t" style="left:67px;width:76px;text-align:center;top:269px;font-size:13px;color:var(--ink)">Monday</div>
  <div class="t" style="left:67px;width:76px;text-align:center;top:285px;font-size:13px;color:var(--ink)">Jan 6th</div>
  <div class="t serif" style="left:190px;width:80px;text-align:center;top:285px;font-size:15px;color:var(--maroon)">JOIN US!</div>
</section>

</body>
</html>
```